Verpackungsetikett für Softeisbecher
Zielgruppe
Wir produzieren Speiseeis, füllen dieses in entsprechende Verpackungseinheiten ab und vermarkten es. Zielgruppe sind alle die, die Eis mögen.
Aufgabenstellung
Das bestehende Etikettendesign (rund 8cm Durchmesser) soll neu überarbeitet werden. Dazu soll es mit unserem neuen Logo (Anhang) versehen werden. Wir freuen uns über fotolose Vorschläge bzw. Design´s mit Foto. Alle Angaben über z.B. Inhaltstoffe, Herstellungdatum, Aufbewahrungtemperatur, Barcode u.s.w.kommen auf ein separates Etikett am Boden des Bechers.Das Erscheinungsbild des Etiketts sollte eine gewisse Neutralität haben, so dass es für die verschiedensten Geschmacksrichtungen verwendet werden kann, sprich ein Etikett für alle Eissorten. Nur der Name der Geschmacksrichtung unterscheidet die Etiketten. Wir verweisen auf einige Link`s ,auf denen man Etikettenbeispiele (z. B. Frischkäse) sieht, die unseren Vorstellungen der Gestaltung entsprechen. Vielen Dank im Voraus

```html
<!DOCTYPE html>
<html lang="de">
<head>
<meta charset="utf-8">
<title>Softeis Etikett</title>
<link rel="stylesheet" href="https://fonts.googleapis.com/css2?family=Baloo+2:wght@700;800&family=Merriweather:ital,wght@1,700&display=swap">
<style>
  :root {
    --sky: #2a9ad6;
    --sky-deep: #1873b8;
    --ink-blue: #14549e;
    --ice-white: #ffffff;
    --mint: #cfe3a6;
    --leaf: #8ab84a;
    --caramel: #d99a3a;
    --caramel-light: #f0c060;
    --cocoa: #b0693a;
    --page: #ffffff;
  }
  html, body {
    margin: 0;
    width: 1200px;
    height: 1200px;
    overflow: hidden;
    background: var(--page);
  }
  .label-canvas {
    display: block;
    width: 1200px;
    height: 1200px;
  }
  .brand-name {
    font-family: "Baloo 2", sans-serif;
    font-weight: 800;
    fill: var(--leaf);
  }
  .product-title {
    font-family: "Baloo 2", sans-serif;
    font-weight: 800;
    fill: var(--ink-blue);
  }
  .claim, .flavour {
    font-family: "Merriweather", serif;
    font-style: italic;
    font-weight: 700;
    fill: var(--ice-white);
  }
</style>
</head>
<body>
<svg class="label-canvas" viewBox="0 0 1200 1200" xmlns="http://www.w3.org/2000/svg">
  <defs>
    <clipPath id="label-disc"><circle cx="600" cy="600" r="500"/></clipPath>
    <clipPath id="label-face"><circle cx="600" cy="600" r="455"/></clipPath>
    <linearGradient id="face-sky" x1="0" y1="0" x2="0" y2="1">
      <stop offset="0" stop-color="#bfe3f6"/>
      <stop offset="0.45" stop-color="#eef7fc"/>
      <stop offset="1" stop-color="#ffffff"/>
    </linearGradient>
    <radialGradient id="face-mint" cx="0.82" cy="0.35" r="0.45">
      <stop offset="0" stop-color="var(--mint)" stop-opacity="0.95"/>
      <stop offset="1" stop-color="var(--mint)" stop-opacity="0"/>
    </radialGradient>
    <radialGradient id="milk-splash" cx="0.5" cy="0.6" r="0.6">
      <stop offset="0" stop-color="#ffffff"/>
      <stop offset="1" stop-color="#e3edf2" stop-opacity="0.6"/>
    </radialGradient>
    <linearGradient id="claim-band" x1="0" y1="0" x2="1" y2="0">
      <stop offset="0" stop-color="var(--caramel)"/>
      <stop offset="1" stop-color="var(--caramel-light)"/>
    </linearGradient>
    <radialGradient id="sweets-tone" cx="0.5" cy="0.55" r="0.55">
      <stop offset="0" stop-color="#8a5634"/>
      <stop offset="0.7" stop-color="#a86e45" stop-opacity="0.85"/>
      <stop offset="1" stop-color="#c89a70" stop-opacity="0"/>
    </radialGradient>
  </defs>

  <g class="label" clip-path="url(#label-disc)">
    <!-- outer ring -->
    <rect class="ring-sky" x="100" y="100" width="1000" height="1000" fill="var(--sky)"/>
    <path class="ring-cocoa" d="M100 820 Q600 760 1100 820 L1100 1100 L100 1100 Z" fill="var(--cocoa)"/>
    <path class="ring-swoosh" d="M160 330 Q420 120 760 150 Q930 165 1050 250 L1060 200 Q900 95 700 105 Q400 110 150 300 Z" fill="var(--ice-white)" opacity="0.9"/>

    <!-- inner face -->
    <g class="label-face" clip-path="url(#label-face)">
      <rect x="145" y="145" width="910" height="910" fill="url(#face-sky)"/>
      <rect x="145" y="145" width="910" height="910" fill="url(#face-mint)"/>
      <path class="face-swoosh" d="M145 300 Q450 150 800 190 Q960 210 1055 270 L1055 145 L145 145 Z" fill="var(--sky)" opacity="0.35"/>
      <rect class="milk-splash" role="img" aria-label="Milchspritzer als Hintergrundfoto" x="145" y="520" width="910" height="535" fill="url(#milk-splash)"/>
      <path class="cocoa-rim" d="M145 1000 Q600 960 1055 1000 L1055 1055 L145 1055 Z" fill="var(--cocoa)"/>
    </g>

    <!-- brand -->
    <circle class="brand-dot" cx="600" cy="270" r="55" fill="var(--sky)" opacity="0.55"/>
    <text class="brand-name" x="600" y="405" text-anchor="middle" font-size="60">Kellerwind</text>

    <!-- product title -->
    <text class="product-title" x="594" y="645" text-anchor="middle" font-size="195" stroke="#ffffff" stroke-width="10" paint-order="stroke" letter-spacing="-3">Softeis</text>

    <!-- claim and flavour bands -->
    <path class="claim-band" d="M100 770 L740 742 L746 838 L100 862 Z" fill="url(#claim-band)"/>
    <text class="claim" x="215" y="830" font-size="56" transform="rotate(-2.5 215 830)">mmh... so lecker!</text>
    <path class="flavour-band" d="M100 862 L746 838 L754 900 L100 928 Z" fill="var(--cocoa)"/>
    <text class="flavour" x="240" y="902" font-size="34" transform="rotate(-2 240 902)">chocolate &amp; vanille</text>

    <!-- flavour picture -->
    <ellipse class="flavour-visual" role="img" aria-label="Foto von Schokoladenstücken mit Vanilleblüte und Vanilleschote" cx="800" cy="900" rx="120" ry="110" fill="url(#sweets-tone)"/>
  </g>
</svg>
</body>
</html>
```